Visitenkarten für Familienunternehmen in den Bereichen Fliesen, Natursteine, Kaminöfen, Schwimmbäder und Whirlpools
Zielgruppe
Wir sind ein Familienunternehmen in dritter Generation und Spezialist für Fliesen, Natursteine, Kaminöfen, Schwimmbäder und Whirlpools. Professionell, kreativ und voller Leidenschaft begleiten wir unsere Kunden bei der Umsetzung ihrer Vorhaben. Von der persönlichen Beratung bis hin zur Ausführung profitieren unsere Kunden von qualifiziertem Fachpersonal und 60 Jahren Erfahrung. Unsere Zielgruppe sind Familien/Paare ab 35 Jahren, die Produkte höchster Qualität für Ihr Zuhause suchen.
Aufgabenstellung
Wir benötigen neue Visitenkarten, da wir ein neues Logo haben. Wir haben folgende Vorstellung:
Rückseite: Komplett schwarz bzw. dunkel (Farbton ähnlich DB703), mittig unser neues Logo in weiß.
Vorderseite: Auch hier Hintergrund schwarz, Logo in weiß, Name des Ansprechpartners samt Titel/Position, Firmenname, Adresse, Telefonnummer, eMail-Adresse und Social Media-Adresse. Des Weiteren sollte unser Portfolio aufgelistet sein (Fliesen, Natursteine, Kaminöfen, Schwimmbäder und Whirlpools). Alternativ können wir uns die Auflistung des Portfolios auch auf der Rückseite vorstellen. Alternativ können wir uns die Vorderseite auch in weiß mit schwarzer Schrift vorstellen.
Der Inhalt der Datei, welche am Ende erstellt wird, muss für unsere Druckerei editierbar sein (Schrift als Text, nicht als Pfad).
Ergänzung 25.03.2023:
Nachdem die ersten Design-Vorschläge eingetroffen sind, haben wir uns dazu entschieden, dass es eine Visitenkarte im Querformat sein soll. Vorder- und Rückseite vollen schwarz/dunkel sein.

```html
<!DOCTYPE html>
<html lang="de">
<head>
<meta charset="utf-8">
<title>Stein-Brok Visitenkarte</title>
<link href="https://fonts.googleapis.com/css2?family=Montserrat:wght@400;600;700&family=Open+Sans:wght@400;600&display=swap" rel="stylesheet">
<style>
  :root {
    --backdrop: #eceeef;
    --card: #232323;
    --ink-light: #ffffff;
    --ink-soft: #cfcfcf;
    --tab: #e3e4e5;
    --tab-ink: #2a2a2a;
  }
  * { margin: 0; padding: 0; box-sizing: border-box; }
  html, body { width: 1200px; height: 720px; overflow: hidden; }
  body {
    background: var(--backdrop);
    font-family: "Open Sans", sans-serif;
    position: relative;
  }
  .card {
    position: absolute;
    top: 185px;
    width: 540px;
    height: 350px;
    background: var(--card);
    color: var(--ink-light);
    overflow: hidden;
    box-shadow: 0 6px 18px rgba(0,0,0,0.18);
  }
  .card--front { left: 40px; }
  .card--back { left: 620px; }

  .brand {
    font-family: "Montserrat", sans-serif;
    font-weight: 600;
    color: var(--ink-light);
    display: flex;
    align-items: center;
    gap: 12px;
    line-height: 1;
  }
  .brand__mark {
    width: 14px; height: 14px;
    background: var(--ink-light);
    flex: none;
  }
  .card--front .brand {
    position: absolute;
    left: 30px; top: 48px;
    font-size: 34px;
  }
  .card--back .brand {
    position: absolute;
    left: 50%; top: 50%;
    transform: translate(-50%, -50%);
    font-size: 44px;
  }

  .contact {
    position: absolute;
    left: 330px; top: 38px;
    list-style: none;
    font-size: 11.5px;
    line-height: 17px;
    color: var(--ink-soft);
  }
  .contact li { display: flex; align-items: flex-start; gap: 8px; }
  .contact svg { width: 12px; height: 12px; margin-top: 2px; flex: none; }
  .contact .indent { padding-left: 20px; }

  .person {
    position: absolute;
    left: 30px; top: 178px;
    font-family: "Montserrat", sans-serif;
  }
  .person__name { font-weight: 700; font-size: 27px; line-height: 32px; }
  .person__role { font-weight: 400; font-size: 20px; line-height: 26px; }

  .portfolio {
    position: absolute;
    left: 30px; top: 262px;
    width: 230px;
  }
  .portfolio__title {
    font-family: "Montserrat", sans-serif;
    font-weight: 700; font-size: 16px; margin-bottom: 3px;
  }
  .portfolio__list { font-size: 11px; line-height: 15px; color: var(--ink-soft); }

  .social {
    position: absolute;
    left: 272px; top: 262px;
    width: 268px; height: 44px;
    background: var(--tab);
    border-radius: 16px 0 0 0;
    display: flex;
    align-items: center;
    justify-content: space-around;
    color: var(--tab-ink);
    font-size: 11.5px;
  }
  .social__item { display: flex; align-items: center; gap: 6px; }
  .social__dot { width: 14px; height: 14px; background: var(--tab-ink); border-radius: 3px; }
</style>
</head>
<body>

<section class="card card--front" aria-label="Vorderseite">
  <div class="brand"><span class="brand__mark"></span>BROK</div>

  <ul class="contact">
    <li>
      <svg viewBox="0 0 12 12" fill="none" stroke="currentColor" stroke-width="1.1"><path d="M6 11s-3.6-3.8-3.6-6.4a3.6 3.6 0 0 1 7.2 0C9.6 7.2 6 11 6 11z"/><circle cx="6" cy="4.6" r="1.3"/></svg>
      <span>Stein-Brok GmbH</span>
    </li>
    <li class="indent">Lindenweg 12</li>
    <li class="indent">54321 Talheim</li>
    <li>
      <svg viewBox="0 0 12 12" fill="currentColor"><path d="M2.6 1.2l2 .2.8 2.4-1.2.9a6.5 6.5 0 0 0 3.1 3.1l.9-1.2 2.4.8.2 2a1 1 0 0 1-1 1A9.6 9.6 0 0 1 1.6 2.2a1 1 0 0 1 1-1z"/></svg>
      <span>0 12 34 - 56 78 90</span>
    </li>
    <li>
      <svg viewBox="0 0 12 12" fill="none" stroke="currentColor" stroke-width="1.1"><rect x="1" y="2.5" width="10" height="7"/><path d="M1 2.5l5 4 5-4"/></svg>
      <span>info@stein-brok.de</span>
    </li>
    <li>
      <svg viewBox="0 0 12 12" fill="none" stroke="currentColor" stroke-width="1"><circle cx="6" cy="6" r="5"/><ellipse cx="6" cy="6" rx="2.2" ry="5"/><path d="M1 6h10M2 3.5h8M2 8.5h8"/></svg>
      <span>www.stein-brok.de</span>
    </li>
  </ul>

  <div class="person">
    <p class="person__name">Timo Brok</p>
    <p class="person__role">Geschäftsführer</p>
  </div>

  <div class="portfolio">
    <p class="portfolio__title">Portfolio:</p>
    <p class="portfolio__list">Fliesen, Natursteine, Kaminöfen,<br>Schwimmbäder und Whirlpools</p>
  </div>

  <div class="social">
    <span class="social__item"><span class="social__dot"></span>@tamebrok</span>
    <span class="social__item"><span class="social__dot"></span>@tamebrok</span>
  </div>
</section>

<section class="card card--back" aria-label="Rückseite">
  <div class="brand"><span class="brand__mark"></span>BROK</div>
</section>

</body>
</html>
```